Biz Card Design TPVC

New business card for a new company.
Logo was completed by a designer on ArtFlock and looking to continue requesting additional services.
Company Name: Tidal Prime Voltage Collective
Although this company is starting in Canada, we will be moving towards a global presence within the next 6 months.
Key elements to this business are as follows.
Energy Procurement
Energy Reduction Services
Demand Side Consulting
Energy Efficiency Consulting
Saving Clients Money
Helping Them Go "Green"
Managing Their Energy Requirements
Basically the goal for our company is to find the best procurement solution for our clients and reduce their energy consumption. This reduces their expenses and the amount of greenhouse gas they produce on a daily basis.
I have been in the energy footprint for the last 20 years and know that most companies are looking to "do whatever is necessary to get them to sign on the dotted line". I would prefer to walk away from a client that I can't help than to put them into a situation that they will regret for years to come. This is where the "TIDAL" part of the company name comes from.
The following is a catch phrase that encompasses what we do.
"Reducing your carbon footprint & energy bill at the same time!"
The back of the card needs to have this statement along with some sort of illustration. The back is a playground for creative ideas.
The front of the card needs the following.
Logo.
First & Last Name (Gus Marwick)
Title (Energy Warrior)
Phone Number (555) 314-2768
Fax Number (555) 862-4091
Email Address gus@tidalprimevoltage.example
Address 47 Orchard Lane Toronto Ontario K4P 2Z7
I want it to be a card that is remembered when any of my staff give it to a customer. It HAS to stand out.
Target Market(s)
Business Owners, Decision Makers, 30 to 65+
Industry/Entity Type
Business
Look and feel
Each slider illustrates characteristics of the customer's brand and the style your logo design should communicate.

```html
<!DOCTYPE html>
<html lang="en">
<head>
<meta charset="utf-8">
<title>Tidal Prime Voltage Collective – Business Card</title>
<link rel="stylesheet" href="https://fonts.googleapis.com/css2?family=Arimo:wght@400;700&family=Questrial&display=swap">
<style>
  :root {
    --canvas: #e9ebe6;
    --card: #ffffff;
    --green: #2f9e44;
    --green-dark: #1f7f32;
    --green-light: #7cc576;
    --green-pale: #dcefd8;
    --blue: #2f5fb3;
    --ink: #333a36;
    --grey: #6a6f6c;
  }
  * { box-sizing: border-box; margin: 0; padding: 0; }
  html, body { width: 1200px; height: 900px; overflow: hidden; }
  body {
    background: var(--canvas);
    font-family: "Questrial", sans-serif;
    display: flex;
    align-items: center;
    justify-content: center;
    gap: 44px;
  }
  .card {
    position: relative;
    width: 540px;
    height: 309px;
    background: var(--card);
    overflow: hidden;
    box-shadow: 0 6px 18px rgba(0,0,0,.15);
  }
  .band-bottom {
    position: absolute; left: 0; right: 0; bottom: 0;
    height: 20px; background: var(--green);
    border-top: 4px solid var(--green-light);
  }

  /* ---------- back: services ---------- */
  .back .header-band {
    position: absolute; top: 0; right: 0;
    width: 330px; height: 40px;
    background: linear-gradient(90deg, var(--green-light), var(--green));
    clip-path: polygon(6% 0, 100% 0, 100% 100%, 0 100%);
    display: flex; align-items: center; justify-content: flex-end;
    padding-right: 14px;
  }
  .wordmark {
    font-family: "Arimo", sans-serif;
    font-weight: 700;
    letter-spacing: -0.3px;
  }
  .back .wordmark { color: #fff; font-size: 16px; }
  .back .emblem-area {
    position: absolute; top: 22px; left: 34px;
    width: 160px; height: 88px;
    border-radius: 50%;
    background: radial-gradient(ellipse at center, var(--green-light), var(--green-pale) 70%, transparent 72%);
  }
  .back .heading {
    position: absolute; left: 34px; top: 128px;
    font-family: "Arimo", sans-serif; font-weight: 700;
    font-size: 17px; color: var(--blue);
  }
  .services {
    position: absolute; top: 160px;
    list-style: none;
    font-size: 12.5px; line-height: 20px; color: var(--grey);
  }
  .services.col-a { left: 40px; }
  .services.col-b { left: 300px; top: 112px; }
  .services li::before {
    content: ""; display: inline-block;
    width: 5px; height: 5px; border-radius: 50%;
    background: var(--green); margin-right: 10px;
    vertical-align: middle;
  }

  /* ---------- front: contact ---------- */
  .front .decor-area {
    position: absolute; top: -20px; right: -40px;
    width: 360px; height: 220px; border-radius: 50%;
    background: radial-gradient(ellipse at 60% 50%, var(--green-pale), rgba(220,239,216,.35) 60%, transparent 72%);
  }
  .front .logo-row {
    position: absolute; left: 0; top: 104px;
    display: flex; align-items: center; gap: 14px;
  }
  .front .logo-tab { width: 8px; height: 26px; background: var(--green); }
  .front .wordmark { color: var(--blue); font-size: 20px; }
  .front .person { position: absolute; left: 96px; top: 150px; }
  .front .name { font-size: 19px; color: var(--ink); }
  .front .title { font-size: 14px; color: var(--green); margin-top: 1px; }
  .contacts {
    position: absolute; left: 96px; top: 200px;
    list-style: none; font-size: 12.5px; color: var(--ink);
  }
  .contacts li { display: flex; align-items: center; height: 19px; gap: 8px; }
  .icon {
    width: 14px; height: 14px; border-radius: 2px;
    background: var(--green); display: inline-flex;
    align-items: center; justify-content: center; flex: none;
  }
  .icon svg { width: 10px; height: 10px; }
  .fax { display: inline-flex; align-items: center; gap: 8px; margin-left: 14px; }
</style>
</head>
<body>

<section class="card back" aria-label="Card back">
  <div class="header-band"><span class="wordmark">TidalPrimeVoltageCollective</span></div>
  <div class="emblem-area" role="img" aria-label="Brand emblem area in green tones"></div>
  <h2 class="heading">Key elements to this business :</h2>
  <ul class="services col-a">
    <li>Energy Procurement</li>
    <li>Energy Reduction Services</li>
    <li>Demand Side Consulting</li>
    <li>Energy Efficiency Consulting</li>
  </ul>
  <ul class="services col-b">
    <li>Saving Clients Money</li>
    <li>Helping Them Go "Green"</li>
    <li>Managing Their Energy Requirements</li>
  </ul>
  <div class="band-bottom"></div>
</section>

<section class="card front" aria-label="Card front">
  <div class="decor-area" role="img" aria-label="Faint large brand decoration in pale green"></div>
  <div class="logo-row">
    <span class="logo-tab"></span>
    <span class="wordmark">TidalPrimeVoltageCollective</span>
  </div>
  <div class="person">
    <p class="name">Gus Marwick</p>
    <p class="title">Energy Warrior</p>
  </div>
  <ul class="contacts">
    <li>
      <span class="icon"><svg viewBox="0 0 10 10"><path d="M5 1 1 5h1.3v4h2V6.5h1.4V9h2V5H9z" fill="#fff"/></svg></span>
      47 Orchard Lane Toronto Ontario K4P 2Z7
    </li>
    <li>
      <span class="icon"><svg viewBox="0 0 10 10"><path d="M2.3 1 3.8 1 4.4 3 3.5 3.8C4 5 5 6 6.2 6.5L7 5.6 9 6.2V7.7C9 8.4 8.4 9 7.7 9 4 9 1 6 1 2.3 1 1.6 1.6 1 2.3 1z" fill="#fff"/></svg></span>
      (555) 314-2768
      <span class="fax">
        <span class="icon"><svg viewBox="0 0 10 10"><rect x="2.5" y="1" width="5" height="3" fill="#fff"/><rect x="1" y="4" width="8" height="4" rx="1" fill="#fff"/><rect x="3" y="6" width="4" height="3" fill="#2f9e44" stroke="#fff" stroke-width=".8"/></svg></span>
        (555) 862-4091
      </span>
    </li>
    <li>
      <span class="icon"><svg viewBox="0 0 10 10"><circle cx="5" cy="5" r="1.6" fill="none" stroke="#fff" stroke-width="1.1"/><path d="M6.6 5v.8c0 .8 1.6.8 1.6-.8A3.2 3.2 0 1 0 7 7.6" fill="none" stroke="#fff" stroke-width="1.1"/></svg></span>
      gus@tidalprimevoltage.example
    </li>
    <li>
      <span class="icon"><svg viewBox="0 0 10 10"><circle cx="5" cy="5" r="3.8" fill="none" stroke="#fff"/><ellipse cx="5" cy="5" rx="1.6" ry="3.8" fill="none" stroke="#fff" stroke-width=".8"/><path d="M1.2 5h7.6" stroke="#fff" stroke-width=".8"/></svg></span>
      www.tidalprimevoltage.example
    </li>
  </ul>
  <div class="band-bottom"></div>
</section>

</body>
</html>
```